Business Card Design for Event Planning Company

Create a business card for event planning company using our new logo. After I pick the design, I will need files made for 6 employees. Our company provides event design & logistics services as well as venue management. The font should be sans serif and complementary to the logo. I will need to know the name of the font selected for the final design. The phone numbers listed should be separated by "." not "-"

Address for the card
PO Box 318, Washington, DC 20019

Card One
Lorna Pettibone
lpettibone@galavoyant.com
202.481.7730

Card Two
Miriam Okonkwo
mokonkwo@galavoyant.com
202.556.2047

Card Three
Tessa Varnholt
tvarnholt@galavoyant.com
978.620.4471

Card Four
Robin Fess
rfess@galavoyant.com
202.718.3362

Card Five
Ada-Rose Pelletan-Uzor
adarose@galavoyant.com
202.839.1205

Card Six
Beatrix Holloway
Beatrix@galavoyant.com
202.492.6618

Target Market(s)

Corporate/Non-Profit

Industry/Entity Type

Event Planning

Contact Information for Business Card

Address for the card

Card One
Lorna Pettibone
lpettibone@galavoyant.com
202.481.7730

Card Two
Miriam Okonkwo
202.556.2047

Card Three
Tessa Varnholt
978.620.4471

Card Four
Robin Fess
rfess@galavoyant.com
202.718.3362

Card Five
Ada-Rose Pelletan-Uzor
202.839.1205

Card Six
Beatrix Holloway
202.492.6618

Font styles to use
Sans Serif

Colors

Designer to choose colors to be used in the design.

Requirements
Must have
• Two-sided with logo
Should not have
• Extra colors or be too busy

```html
<!DOCTYPE html>
<html lang="en">
<head>
<meta charset="utf-8">
<title>Lorna Pettibone – Business Card</title>
<link rel="stylesheet" href="https://fonts.googleapis.com/css2?family=Dancing+Script:wght@700&family=Questrial&display=swap">
<style>
  :root {
    --card-bg: #ffffff;
    --teal: #5ea5a4;
    --teal-name: #5a9e9c;
    --teal-light: #bcdcdb;
    --ink: #111111;
    --band-text: #ffffff;
  }
  html, body {
    margin: 0;
    padding: 0;
    width: 1200px;
    height: 686px;
    overflow: hidden;
    background: var(--card-bg);
  }
  .card {
    position: relative;
    width: 1200px;
    height: 686px;
    background: var(--card-bg);
    overflow: hidden;
    font-family: "Questrial", "Century Gothic", sans-serif;
  }
  .lace-corner {
    position: absolute;
    left: 0;
    top: 0;
    width: 600px;
    height: 380px;
  }
  .contact {
    position: absolute;
    right: 174px;
    top: 196px;
    text-align: right;
    color: var(--ink);
  }
  .contact__name {
    margin: 0 0 8px;
    font-family: "Dancing Script", cursive;
    font-weight: 700;
    font-size: 104px;
    line-height: 1.1;
    color: var(--teal-name);
  }
  .contact__line {
    margin: 0;
    font-size: 39px;
    line-height: 56px;
  }
  .band {
    position: absolute;
    left: 0;
    bottom: 0;
    width: 100%;
    height: 165px;
    background: var(--teal);
  }
  .band__address {
    position: absolute;
    left: 75px;
    top: 58px;
    margin: 0;
    font-size: 38px;
    color: var(--band-text);
  }
  .lace-band {
    position: absolute;
    right: 0;
    bottom: 0;
    width: 390px;
    height: 165px;
  }
</style>
</head>
<body>
  <div class="card">
    <svg class="lace-corner" viewBox="0 0 600 380" role="img" aria-label="Teal lace floral ornament in the top-left corner">
      <defs>
        <radialGradient id="laceTop" cx="0.1" cy="0.15" r="0.9">
          <stop offset="0" stop-color="#8fc2c1" stop-opacity="0.85"/>
          <stop offset="1" stop-color="#bcdcdb" stop-opacity="0.25"/>
        </radialGradient>
      </defs>
      <path d="M0 0 H580 Q560 30 470 28 Q380 32 330 10 Q300 40 270 70 Q240 110 260 160 Q285 220 240 270 Q200 330 130 350 Q60 370 0 330 Z" fill="url(#laceTop)"/>
    </svg>

    <div class="contact">
      <p class="contact__name">Lorna Pettibone</p>
      <p class="contact__line">lpettibone@galavoyant.com</p>
      <p class="contact__line">202.481.7730</p>
    </div>

    <div class="band">
      <p class="band__address">PO Box 318, Washington, DC 20019</p>
      <svg class="lace-band" viewBox="0 0 390 165" role="img" aria-label="White lace doily ornament on the bottom-right of the band">
        <defs>
          <radialGradient id="laceBand" cx="0.75" cy="0.6" r="0.7">
            <stop offset="0" stop-color="#ffffff" stop-opacity="0.75"/>
            <stop offset="1" stop-color="#ffffff" stop-opacity="0.15"/>
          </radialGradient>
        </defs>
        <path d="M30 165 Q20 120 70 100 Q110 90 140 60 Q190 10 260 0 H390 V165 Z" fill="url(#laceBand)"/>
      </svg>
    </div>
  </div>
</body>
</html>
```